D/L brochure 97mm deep x 210mm wide 4 colour printed both sides.

Copy is written.

Desin brief is to promote the fact that Marlow Electrical are the bright sparks in electrical contracting.
That Marlow Electrical are honest, reliable, and do a quality job.
Updates

Brochrue will be an embedded email E-brochure). can you link it to

www.marlowelectrical.com.au

Target Market(s)

Commercial builders, office and shop fitters.

Industry/Entity Type

Electrical

Requirements
Must have
• Use the copy attached
• include the response details
Nice to have
• Some design that positions Marlow Electrical as bright sparks.
• As quality company
• As reliable.

```html
<!DOCTYPE html>
<html lang="en">
<head>
<meta charset="utf-8">
<title>Marlow Electrical – The bright sparks in electrical contracting</title>
<link href="https://fonts.googleapis.com/css2?family=Arimo:wght@400;700&family=Marcellus&family=Roboto+Condensed:wght@400;700&display=swap" rel="stylesheet">
<style>
  :root {
    --lime: #d2e21b;
    --lime-light: #eef58a;
    --lime-deep: #bccc0c;
    --navy: #1f2470;
    --ink: #2a2a22;
    --accent: #c8202a;
    --rule: #f4f8c8;
    --bulb-glow: #ffffff;
  }
  * { box-sizing: border-box; margin: 0; padding: 0; }
  html, body { width: 1200px; height: 1111px; overflow: hidden; background: #ffffff; }
  body { font-family: "Arimo", Arial, sans-serif; color: var(--ink); }

  .brochure { position: relative; width: 1200px; height: 1111px; overflow: hidden; }

  .panel {
    position: absolute; left: 0; width: 1200px;
    background: radial-gradient(ellipse at 50% 55%, var(--lime-light) 0%, var(--lime) 55%, var(--lime-deep) 100%);
  }
  .panel--front { top: 0; height: 556px; }
  .panel--back { top: 558px; height: 553px; }
  .panel-divider { position: absolute; left: 0; top: 556px; width: 1200px; height: 2px; background: var(--rule); }

  .bulb {
    position: absolute;
    background: radial-gradient(ellipse at 45% 45%, var(--bulb-glow) 0%, #fbfdf0 45%, rgba(255,255,255,0.55) 70%, rgba(255,255,255,0) 100%);
    border-radius: 50%;
  }

  .brand-name {
    position: absolute; font-family: "Roboto Condensed", Arial, sans-serif;
    font-weight: 700; color: var(--navy); line-height: 1;
  }
  .brand-name--main { left: 60px; top: 34px; font-size: 56px; width: 360px; line-height: 1.0; }
  .contact-person {
    position: absolute; left: 122px; top: 152px;
    font-family: "Arimo", Arial, sans-serif; font-weight: 700; font-size: 19px;
    color: var(--navy); letter-spacing: 0.5px;
  }

  .headline {
    position: absolute; right: 22px; top: 26px;
    font-family: "Roboto Condensed", Arial, sans-serif; font-weight: 700;
    font-size: 30px; color: var(--navy); text-align: right;
  }
  .company-line {
    position: absolute; right: 22px; top: 80px;
    font-family: "Roboto Condensed", Arial, sans-serif; font-size: 28px;
    color: var(--navy); text-align: right;
  }
  .tagline-line {
    position: absolute; right: 22px; top: 124px;
    font-family: "Roboto Condensed", Arial, sans-serif; font-size: 23px;
    color: var(--navy); text-align: right;
  }

  .values {
    position: absolute; left: 86px; top: 586px;
    font-family: "Marcellus", Georgia, serif; font-size: 31px; color: var(--navy);
    white-space: nowrap;
  }
  .values strong { font-weight: 700; -webkit-text-stroke: 0.6px var(--navy); }
  .values .sep { color: var(--accent); margin: 0 8px; }
  .values .difference { margin-left: 50px; }

  .body-copy {
    position: absolute; left: 88px; top: 642px; width: 1090px;
    font-size: 16.6px; line-height: 23.5px; color: var(--ink);
  }

  .brand-name--small { left: 0; width: 1200px; top: 900px; font-size: 40px; text-align: center; }
  .contact-person--small { left: 0; width: 1200px; top: 952px; font-size: 11px; text-align: center; }
  .brand-tagline {
    position: absolute; left: 0; width: 1200px; top: 978px; text-align: center;
    font-size: 15px; letter-spacing: 3.2px; color: var(--ink);
  }

  .footer {
    position: absolute; left: 172px; top: 1060px;
    font-size: 19.5px; color: var(--ink); white-space: nowrap;
  }
  .footer strong { color: var(--ink); }
  .footer .sep { color: var(--accent); margin: 0 6px; }
</style>
</head>
<body>
<main class="brochure">
  <section class="panel panel--front">
    <div class="bulb" style="left:60px; top:186px; width:520px; height:360px;" role="img" aria-label="Glowing light bulb lying on its side"></div>
    <div class="bulb" style="left:700px; top:186px; width:490px; height:350px;" role="img" aria-label="Second glowing light bulb lying on its side"></div>

    <div class="brand-name brand-name--main">Marlow<br>Electrical</div>
    <div class="contact-person">DANIEL HARTLEY</div>

    <h1 class="headline">Seeking that spark of intelligence from your contractor?</h1>
    <p class="company-line">Marlow Electrical</p>
    <p class="tagline-line">- the bright sparks in electrical contracting</p>
  </section>

  <div class="panel-divider"></div>

  <section class="panel panel--back">
    <div class="bulb" style="left:20px; top:350px; width:400px; height:240px;" role="img" aria-label="Glowing light bulb"></div>
    <div class="bulb" style="left:720px; top:440px; width:170px; height:140px;" role="img" aria-label="Small glowing light bulb"></div>
    <div class="bulb" style="left:905px; top:350px; width:290px; height:230px;" role="img" aria-label="Glowing light bulb seen from the base"></div>
  </section>

  <h2 class="values">
    <strong>Honesty</strong><span class="sep">|</span><strong>Integrity</strong><span class="sep">|</span><strong>Reliability</strong>
    <span class="difference">That’s the Marlow Electrical difference</span>
  </h2>

  <div class="body-copy">
    <p>Intelligent people with a work ethic who get the job done on time for the agreed price are hard to find. But perhaps you haven’t used Marlow Electrical before?</p>
    <p>Marlow Electrical are the quality alternative in electrical contracting. What they say they’ll do, they do. No arguments, no short cuts.</p>
    <p>From commercial building construction, shop or office fit-outs, factory units or repairs, through to commercial property maintenance, Marlow Electrical deliver quality outcomes with the service you rightly expect.</p>
    <p>If you want the job finished on time, call Daniel Hartley at Marlow Electrical on 02 9555 0142 or 0400 555 218. Alternatively, email Daniel at dhartley@marlowelectrical.com.au</p>
  </div>

  <div class="brand-name brand-name--small">Marlow Electrical</div>
  <div class="contact-person contact-person--small">DANIEL HARTLEY</div>
  <p class="brand-tagline">The bright sparks in electrical contracting</p>

  <p class="footer"><strong>Marlow Electrical</strong><span class="sep">|</span>4/21-23 Kestrel Place<span class="sep">|</span>Greystone Park NSW 2170<span class="sep">|</span>ABN 12 345 678 901</p>
</main>
</body>
</html>
```